Für das neue Tantra-Bildungszetrum: 8-oder 10-Seiten-Faltblatt und ein Plakat DIN A3
Zielgruppe
Es geht darum, über das Angebot des neuen Bildungszentrums Kreis der Morgenröte zu informieren.
Das Zentrum organisiert und führt regelmäßige Veranstaltungen wie Info-Vorträge, Schnuppertage, Seminare, Kurse und Intensivtrainings durch, ist in allem spezialisiert auf Tantra. Das Zentrum ist vertreten an mehreren Standorten Deutschlands durch das jeweils ein Team an Lehrern und Dozenten. Für die Veranstaltungen werden externe Räume angemietet. Das Angebot soll in jeder Stadt, wo die Broschüren oder Faltblätter verteilt werden. Die Anmeldung und Registrierung erfolgt über die neue Homepage, die bald freigegeben wird und noch nicht zur Verfügung steht.
Das Besondere am Zentrum ist die Möglichkeit, eigene tantrische Selbsterfahrungen zu machen und entweder später oder als Option sich gleich für einen der sechs neuen Tantra- Ausbildungsberufe zu entscheiden.
Darüber hinaus, soll die Broschüre oder die Faltblätter zur Mitarbeit und Kooperation mit selbständigen Yoga- und Tantra-Lehrern, sowie Ärzten, Therapeuten und Heilpraktiken einladen.
Das Bildungszentrum ist ein Netzwerk der Honorar-Dozenten, die entweder Lehrer und Experte auf dem tantrischen Bereich oder Vertreter der klassischen und alternativen Heilkunde oder beides zusammen sind.
Wer ist die Zielgruppe? Männer und Frauen, vom 18 - 60 Jahre. Menschen, die sich für Tantra und Selbsterfahrung interessieren, und Menschen, die nach einer neuen beruflichen Perspektive suchen.
Aufgabenstellung
1). 10-Seiten- Faltblatt designen
2). Plakat DIN A3 gestalten

```html
<!DOCTYPE html>
<html lang="de">
<head>
<meta charset="utf-8">
<title>Bildungszentrum Kreis der Morgenröte – Plakat</title>
<link rel="stylesheet" href="https://fonts.googleapis.com/css2?family=Arimo:wght@400;700&family=Tinos:wght@400;700&family=Parisienne&display=swap">
<style>
  :root {
    --green: #2c6b54;
    --green-dark: #245a46;
    --orange: #e8772a;
    --ink: #3a3a3a;
    --paper: #ffffff;
    --ornament: #f6d3b6;
    --photo-warm: #c9702e;
    --photo-deep: #7a3212;
  }
  * { box-sizing: border-box; margin: 0; padding: 0; }
  html, body { width: 849px; height: 1200px; overflow: hidden; background: var(--paper); }
  .poster { position: relative; width: 849px; height: 1200px; background: var(--paper); font-family: "Arimo", Arial, sans-serif; color: var(--ink); }

  .brand { position: absolute; left: 186px; top: 62px; display: flex; align-items: center; gap: 20px; }
  .brand-dot { width: 84px; height: 84px; border-radius: 50%; background: var(--orange); }
  .brand-name { color: var(--green); font-weight: 700; line-height: 1.05; }
  .brand-name .line-1 { display: block; font-size: 36px; }
  .brand-name .line-2 { display: block; font-size: 50px; }

  .intro { position: absolute; left: 18px; top: 210px; width: 552px; height: 368px; background: var(--green); padding: 24px 22px 0 20px; }
  .intro p { font-family: "Tinos", "Times New Roman", serif; color: #fff; font-size: 15.4px; line-height: 22.4px; text-align: justify; hyphens: auto; }
  .intro p::first-letter { font-size: 26px; }
  .intro-photo { position: absolute; left: 570px; top: 210px; width: 279px; height: 368px; background: radial-gradient(circle at 55% 45%, var(--photo-warm), var(--photo-deep)); }

  .offer { position: absolute; font-size: 14px; line-height: 19px; }
  .offer h3 { font-size: 14px; line-height: 19px; font-weight: 700; color: var(--green); }
  .offer .accent { color: var(--orange); }
  .offer ol, .offer ul { list-style: none; color: var(--ink); }
  .offer-rule { position: absolute; height: 1px; background: var(--green); }
  .ornament { position: absolute; border-radius: 50%; background: var(--ornament); }

  .tagline { position: absolute; left: 40px; top: 900px; width: 400px; text-align: center; font-family: "Parisienne", cursive; color: var(--green); font-size: 31px; line-height: 40px; }

  .portrait { position: absolute; left: 120px; top: 1013px; width: 166px; height: 166px; border-radius: 50%; border: 4px solid var(--green); background: radial-gradient(circle at 50% 40%, #b89b84, #5a4a3f); }

  .contact-title { position: absolute; left: 357px; top: 1016px; font-size: 22px; font-weight: 700; color: var(--green); }
  .contact { position: absolute; left: 292px; top: 1047px; width: 557px; height: 153px; background: var(--green); padding: 12px 0 0 30px; }
  .contact li { list-style: none; display: flex; align-items: center; gap: 12px; height: 33.5px; color: #fff; font-weight: 700; font-size: 19px; }
  .contact-icon { width: 22px; height: 22px; flex: none; }
  .contact-icon.plain { border-radius: 50%; background: #fff; }
  .contact-icon.square { background: #fff; }
</style>
</head>
<body>
<div class="poster">

  <header class="brand">
    <span class="brand-dot"></span>
    <span class="brand-name"><span class="line-1">Bildungszentrum</span><span class="line-2">Kreis der Morgenröte</span></span>
  </header>

  <section class="intro">
    <p>Unser Bildungszentrum soll viele Menschen bei ihren inneren Transformationsprozessen unterstützen indem es spezielle berufliche Perspektiven anbietet, bei denen Selbstverwirklichung in authentischem Kontakt mit anderen Menschen möglich ist. Wenn die innere Welt in Frieden, Harmonie und Ruhe ist, so wird sich dies auch auf unsere äußere Welt auswirken und initiiert so einen Gesellschaftwandel durch innere Transformation. Tantra liefert uns Techniken, die unser Bewusstsein durch die Transformation innerer Vorgänge grundlegend wandeln. Tantra unterstützt Menschen in ihrem Bemühen um spirituelles Wachstum, Selbstverwirklichung, innere Entwicklung sowie der Verbesserung ihrer Liebes- und Lustfähigkeit. Es fördert das Aufblühen der eigenen inneren Göttlichkeit und das Nutzen von sexueller Energie im spirituellen Sinne. Dies ist nur kleiner Ausschnitt dessen, was Tantra uns ermöglicht.</p>
  </section>
  <div class="intro-photo" role="img" aria-label="Foto: Paar in warmem, orangefarbenem Licht bei einer tantrischen Berührung"></div>

  <div class="ornament" style="left:24px;top:626px;width:100px;height:100px" role="img" aria-label="Orangefarbenes Mandala-Ornament"></div>
  <div class="offer" style="left:135px;top:618px;width:270px">
    <h3>Wir laden dich herzlich zu unseren <span class="accent">regelmäßigen Vorträgen</span> ein:</h3>
    <ol><li>1. Was ist Tantra?</li><li>2. Berufliche Perspektiven mit Tantra.</li></ol>
  </div>
  <div class="offer-rule" style="left:135px;top:720px;width:262px"></div>

  <div class="ornament" style="left:24px;top:775px;width:100px;height:100px" role="img" aria-label="Orangefarbenes Mandala-Ornament"></div>
  <div class="offer" style="left:135px;top:747px;width:270px">
    <h3>Steige ein in den nächsten <span class="accent">12- Wochen Tantra-Kurs:</span></h3>
    <ul style="margin-top:12px;padding-left:10px">
      <li>•&nbsp; "Tantra für Anfänger"</li>
      <li>•&nbsp; "Tantra für Mittelstufe"</li>
      <li>•&nbsp; "Tantra für Fortgeschrittene"</li>
    </ul>
  </div>

  <div class="ornament" style="left:428px;top:616px;width:92px;height:92px" role="img" aria-label="Orangefarbenes Mandala-Ornament"></div>
  <div class="offer" style="left:532px;top:616px;width:300px">
    <h3>Erfahre den Geschmack, den Geruch, die Farbe und den Klang von Tantra bei einem unserer <span class="accent">Schnuppertage oder Einsteiger-Wochenenden.</span></h3>
  </div>
  <div class="offer-rule" style="left:532px;top:720px;width:305px"></div>

  <div class="ornament" style="left:428px;top:778px;width:92px;height:92px" role="img" aria-label="Orangefarbenes Mandala-Ornament"></div>
  <div class="offer" style="left:532px;top:745px;width:305px">
    <h3>Mach Tantra zu deinem Beruf! Investiere zwei bis fünf wundervolle Jahre je nach deiner Wahl in eine <span class="accent">Berufsausbildung mit Zukunft!</span><br>Welche unserer sechs Ausbildungsberufe spricht dich an?</h3>
    <ol style="margin-top:18px">
      <li>1. Tantra-Lehrer</li>
      <li>2. Tantra-Yoga-Lehrer</li>
      <li>3. Tantrischer Massagetherapeut</li>
      <li>4. Tantrischer Sexualtherapeut</li>
      <li>5. Tantra-Coach</li>
      <li>6. Selbst Ausbilder werden</li>
    </ol>
  </div>

  <p class="tagline">Wir sind ein wachsendes Netzwerk<br>aus mehreren Lehrern.</p>

  <div class="portrait" role="img" aria-label="Porträtfoto einer Lehrerin des Zentrums"></div>

  <h2 class="contact-title">Kontakt:</h2>
  <ul class="contact">
    <li><span class="contact-icon plain"></span>www.morgenroete-kreis.de</li>
    <li>
      <svg class="contact-icon" viewBox="0 0 24 24"><circle cx="12" cy="12" r="12" fill="#fff"/><path d="M8 6.5c.6-.4 1.3-.3 1.6.3l1 1.8c.3.5.2 1.1-.3 1.4l-.8.6c.6 1.4 1.7 2.5 3.1 3.1l.6-.8c.3-.5.9-.6 1.4-.3l1.8 1c.6.3.7 1 .3 1.6l-.7.9c-.5.6-1.3.8-2 .5-3.3-1.2-5.8-3.7-7-7-.3-.7-.1-1.5.5-2z" fill="#2c6b54"/></svg>
      0176 31 52 74 06
    </li>
    <li><span class="contact-icon square"></span>Tantra.Bildungszentrum.KreisDerMorgenroete</li>
    <li><span class="contact-icon square"></span>KreisDerMorgenroete</li>
  </ul>

</div>
</body>
</html>
```